Business card for STEADYLINE

Please design professional business card for IT consulting firm STEADYLINE INC.
Use logo attached.
Use information from sample tRove business card attached.
replace trove inc with STEADYLINE INC.
as well as troveinc.com with steadyline.example

```html
<!DOCTYPE html>
<html lang="en">
<head>
<meta charset="utf-8">
<title>STEADYLINE business card</title>
<link rel="stylesheet" href="https://fonts.googleapis.com/css2?family=Montserrat:wght@700&family=Open+Sans:wght@400;700&display=swap">
<style>
:root{
  --page:#2a2a2a;
  --card-white:#ffffff;
  --card-black:#111111;
  --ink:#141414;
  --muted:#555555;
  --purple:#6b2a93;
  --icon-blue:#3aa3e0;
  --faint:#ededed;
  --band:linear-gradient(90deg,#6b2a93 0%,#6fc7a8 35%,#4fc0ee 65%,#c9a870 85%,#f7931e 100%);
}
*{margin:0;padding:0;box-sizing:border-box}
html,body{width:1200px;height:900px;overflow:hidden;background:var(--page)}
.stage{position:relative;width:1200px;height:900px}
.card{position:absolute;left:270px;width:660px;height:377px;overflow:hidden;box-shadow:0 10px 30px rgba(0,0,0,.45)}
.card-front{top:40px;background:var(--card-white)}
.card-back{top:475px;background:var(--card-black)}
.wordmark{font-family:"Montserrat",sans-serif;font-weight:700;letter-spacing:.12em;display:flex;align-items:center;gap:14px}
.wordmark-mark{display:inline-block;width:22px;height:22px;background:var(--purple)}
.card-front .wordmark{position:absolute;left:40px;top:34px;font-size:46px;color:var(--ink)}
.faint-square{position:absolute;right:70px;top:150px;width:190px;height:190px;background:var(--faint)}
.person{position:absolute;left:40px;top:112px;font-family:"Open Sans",sans-serif}
.person-name{font-size:17px;font-weight:700;color:var(--purple);letter-spacing:.02em;text-transform:uppercase}
.person-title{font-size:15px;color:var(--muted);margin-top:2px}
.divider{position:absolute;left:40px;right:40px;top:178px;height:1.5px;background:var(--purple)}
.contacts{position:absolute;left:40px;top:198px;list-style:none;font-family:"Open Sans",sans-serif;font-size:14px;color:var(--muted);line-height:23px}
.contacts li{display:flex;align-items:center;gap:8px}
.contacts svg{width:13px;height:13px;flex:none}
.address{position:absolute;right:40px;top:198px;text-align:right;font-family:"Open Sans",sans-serif;font-size:14px;color:var(--muted);line-height:21px}
.address-company{color:var(--ink);font-size:15px;margin-bottom:2px}
.colour-band{position:absolute;left:0;right:0;bottom:0;height:9px;background:var(--band)}
.card-back .wordmark{position:absolute;left:0;right:0;top:0;bottom:0;justify-content:center;font-size:50px;color:#ffffff}
</style>
</head>
<body>
<main class="stage">
  <section class="card card-front" aria-label="Business card front">
    <div class="wordmark"><span>STEADYLINE</span><span class="wordmark-mark"></span></div>
    <div class="faint-square"></div>
    <div class="person">
      <p class="person-name">Dorian Vellacott, P.Eng.</p>
      <p class="person-title">General Manager</p>
    </div>
    <div class="divider"></div>
    <ul class="contacts">
      <li><svg viewBox="0 0 16 16"><path fill="var(--icon-blue)" d="M3 1l3 3-1.5 2a9 9 0 0 0 5.5 5.5L12 10l3 3-2 2C6 15 1 10 1 3z"/></svg>(555) 014-2270 ext.201</li>
      <li><svg viewBox="0 0 16 16"><rect x="4" y="1" width="8" height="14" rx="1.5" fill="none" stroke="var(--icon-blue)" stroke-width="1.6"/></svg>(555) 019-3384</li>
      <li><svg viewBox="0 0 16 16"><rect x="1" y="3" width="14" height="10" fill="var(--icon-blue)"/><path d="M1 3l7 6 7-6" fill="none" stroke="#fff" stroke-width="1.3"/></svg>dvellacott@steadyline.example</li>
      <li><svg viewBox="0 0 16 16"><circle cx="8" cy="8" r="6.5" fill="none" stroke="var(--icon-blue)" stroke-width="1.6"/><path d="M1.5 8h13M8 1.5c-3 3.5-3 9.5 0 13M8 1.5c3 3.5 3 9.5 0 13" fill="none" stroke="var(--icon-blue)" stroke-width="1.2"/></svg>www.steadyline.example</li>
    </ul>
    <address class="address">
      <p class="address-company">STEADYLINE INC.</p>
      <p>1820 Harbourview Rd, Suite 101</p>
      <p>Lakefield, Ontario</p>
      <p>K0A 1B0, Canada</p>
    </address>
    <div class="colour-band"></div>
  </section>
  <section class="card card-back" aria-label="Business card back">
    <div class="wordmark"><span>STEADYLINE</span><span class="wordmark-mark"></span></div>
  </section>
</main>
</body>
</html>
```